Handout for attendees of educational seminar

I provide educational workshops on how to give technical presentations at conferences to scientists and engineers. My company is called Craft Talk Studio (www.CraftTalkStudio.example). I would like a double sided, half page size flyer that can be used as a handout for attendees of my workshops. On one side of the flyer, they will get top tips for creating their next presentation. On the other side, they will get my photo, bio, and contact information. I have uploaded a draft of a full page design I made myself. I'd like the copy of the tips to remain the same, but everything else is flexible.

Target Market(s)

scientists, engineers, technical professionals

Font styles to use
Serif
Sans Serif

Requirements
Must have
• my photo (I've provided two options to choose from depending on colors...photo on side 2 only), my logo, flyer needs to be half page in size (5.5" x 8.5"), needs to be double sided, One side has the "tips" and the other side has my personal details (see attached page for copy).
Nice to have
• I like the use of icons on the "tips" side of the flyer.

```html
<!DOCTYPE html>
<html lang="en">
<head>
<meta charset="utf-8">
<title>Craft Talk Studio – Workshop Handout</title>
<link href="https://fonts.googleapis.com/css2?family=Hind:wght@400;600&family=Montserrat:wght@500;700;800&display=swap" rel="stylesheet">
<style>
:root{
  --teal:#4497b5;
  --green:#8aac5e;
  --ink:#4a4a4a;
  --grey:#5f5f5f;
  --paper:#fbfbfc;
  --paper-shade:#eceef1;
  --stage:#ffffff;
}
*{box-sizing:border-box;margin:0;padding:0}
html,body{width:1200px;height:1000px;overflow:hidden;background:var(--stage)}
body{position:relative;font-family:"Hind",Arial,sans-serif;color:var(--ink)}
.page{position:absolute;background:linear-gradient(160deg,var(--paper) 0%,var(--paper-shade) 55%,var(--paper) 100%);overflow:hidden}
.page--bio{left:32px;top:80px;width:553px;height:855px}
.page--tips{left:608px;top:80px;width:555px;height:860px}

/* bio side */
.bio-band{position:absolute;left:0;top:290px;width:100%;height:438px;background:var(--teal)}
.portrait-ring{position:absolute;left:22px;top:44px}
.portrait{position:absolute;left:22px;top:43px;width:322px;height:322px;border-radius:50%;
  background:radial-gradient(circle at 50% 40%,#e9c7ab 0%,#b98a5e 38%,#2f8b5c 75%,#cfd6d6 100%)}
.meet{position:absolute;left:400px;top:102px;text-align:right;width:120px}
.meet__small{display:block;font-family:"Montserrat",sans-serif;font-weight:500;font-size:38px;color:var(--grey);line-height:1}
.meet__name{display:block;font-family:"Montserrat",sans-serif;font-weight:800;font-size:38px;color:var(--green);line-height:1.1}
.bio-text{position:absolute;left:38px;top:376px;width:478px;color:#fff;font-size:14.6px;line-height:16.3px}
.bio-text p{margin-bottom:16px}
.bio-text strong{font-weight:600}
.brand{position:absolute;text-align:center}
.brand--bio{left:25px;top:740px;width:170px}
.brand__dot{display:block;margin:0 auto 6px;width:58px;height:58px;border-radius:50%;background:#5d5d5d}
.brand__name{font-size:21px;color:var(--green);font-weight:400;line-height:1}
.contact{position:absolute;right:20px;top:768px;text-align:right;font-size:14.5px;color:var(--green)}
.contact li{list-style:none;display:flex;justify-content:flex-end;align-items:center;gap:8px;height:25px}

/* tips side */
.tips-kicker{position:absolute;top:31px;width:100%;text-align:center;font-size:22px;line-height:1.2;color:var(--grey)}
.tips-title{position:absolute;top:58px;width:100%;text-align:center;font-family:"Montserrat",sans-serif;font-weight:800;font-size:64px;letter-spacing:1px;color:var(--green);line-height:1}
.tips-rule{position:absolute;left:80px;top:126px;width:403px;height:2px;background:var(--teal)}
.tips-motto{position:absolute;top:131px;width:100%;text-align:center;font-family:"Montserrat",sans-serif;font-weight:700;font-size:13.8px;line-height:18px;color:var(--ink)}
.tip{position:absolute;left:60px;width:423px;height:160px}
.tip__badge{position:absolute;left:0;top:0;width:160px;height:160px;border-radius:50%;border:2.5px solid var(--teal);background:#fff;display:flex;align-items:center;justify-content:center}
.tip__art{width:120px;height:120px;border-radius:50%;background:radial-gradient(circle,#8a8a8a 0%,#5d5d5d 60%,#e6e6e6 100%)}
.tip__head{position:absolute;left:157px;top:12px;width:266px;height:36px;background:var(--teal);border-top-right-radius:12px;color:#fff;font-family:"Montserrat",sans-serif;font-weight:700;font-size:15.5px;display:flex;align-items:center;justify-content:center}
.tip__body{position:absolute;left:157px;top:48px;width:266px;height:104px;border:2px solid var(--teal);border-left:none;border-bottom-right-radius:12px;background:#fff;padding:7px 8px 0 28px;font-size:10.3px;line-height:12.6px;color:#555;text-align:justify}
.tip__body p+p{margin-top:10px}
.tip--1{top:178px}
.tip--2{top:376px}
.tip--3{top:572px}
.tips-foot-mark{position:absolute;left:0;top:782px;width:20px;height:48px;background:var(--teal)}
.brand--tips{left:22px;top:768px;width:140px}
.brand--tips .brand__dot{width:50px;height:50px;margin-bottom:2px}
.brand--tips .brand__name{font-size:17px}
.tips-cta{position:absolute;left:167px;top:785px;width:388px;height:45px;background:var(--teal);color:#fff;font-weight:600;font-size:11.8px;line-height:14px;text-align:center;padding:8px 14px 0}
</style>
</head>
<body>

<section class="page page--bio" aria-label="About side">
  <div class="bio-band"></div>
  <svg class="portrait-ring" width="350" height="340" viewBox="0 0 350 340" aria-hidden="true">
    <circle cx="172" cy="170" r="162" fill="none" stroke="var(--teal)" stroke-width="1.5"/>
    <path d="M40 60 A165 165 0 0 1 330 150" fill="none" stroke="var(--green)" stroke-width="1.2"/>
    <path d="M338 180 A168 168 0 0 1 250 318" fill="none" stroke="var(--green)" stroke-width="1.2"/>
  </svg>
  <div class="portrait" role="img" aria-label="Portrait photo of Dana Whitfield"></div>
  <h1 class="meet"><span class="meet__small">meet</span><span class="meet__name">DANA</span></h1>

  <div class="bio-text">
    <p>Dana Whitfield is on a mission: to transform how scientists, engineers, and technical professionals present their work. That’s because she believes that even the best technical ideas are destined to remain undiscovered unless presented in a clear and compelling way that sparks innovation and drives adoption.</p>
    <p>For a decade, she’s traveled around the world to work with Top 100 corporations, institutions and universities, teaching the proven strategies she’s mastered through her consulting work and during her time as a faculty member Northfield State University.</p>
    <p>Dana is internationally known for her popular IdeaStage Talk entitled <strong>"Speak Geek to Me"</strong> which has over 2 million views (and counting!).</p>
    <p>Teams that work with Dana get the practical skills and natural confidence they need to immediately shift their “information dump”-style presentations into ones that are meaningful, engaging, and inspire people to take action. Dana provides on-site group workshops and coaching, conference sessions and keynotes, and 1:1 consultation.</p>
  </div>

  <div class="brand brand--bio">
    <span class="brand__dot"></span>
    <span class="brand__name">Dana Whitfield</span>
  </div>

  <ul class="contact">
    <li>www.CraftTalkStudio.example
      <svg width="20" height="20" viewBox="0 0 20 20" aria-hidden="true"><circle cx="10" cy="10" r="10" fill="#666"/><circle cx="10" cy="10" r="6" fill="none" stroke="#fff" stroke-width="1.2"/><path d="M4 10h12M10 4v12M10 4c-3 3-3 9 0 12M10 4c3 3 3 9 0 12" fill="none" stroke="#fff" stroke-width="1"/></svg></li>
    <li>dana@crafttalkstudio.example
      <svg width="20" height="20" viewBox="0 0 20 20" aria-hidden="true"><circle cx="10" cy="10" r="10" fill="#666"/><rect x="4.5" y="6.5" width="11" height="7.5" fill="none" stroke="#fff" stroke-width="1.2"/><path d="M4.5 6.5l5.5 4.5 5.5-4.5" fill="none" stroke="#fff" stroke-width="1.2"/></svg></li>
  </ul>
</section>

<section class="page page--tips" aria-label="Tips side">
  <p class="tips-kicker">Craft Talk Studio</p>
  <h2 class="tips-title">QUICK TIPS</h2>
  <div class="tips-rule"></div>
  <p class="tips-motto">Science not communicated is science not done!</p>

  <article class="tip tip--1">
    <div class="tip__badge"><div class="tip__art" role="img" aria-label="Icon of a speaker's podium facing an audience"></div></div>
    <h3 class="tip__head">BE AUDIENCE CENTERED</h3>
    <div class="tip__body">
      <p>Your ability to be successful as a speaker depends upon your ability to make your audience successful.</p>
      <p><strong>TIP:</strong> Return to "Points of Common Ground" throughout the talk that answer the question "So what?" about the scientific info. Be an interpreter!</p>
    </div>
  </article>

  <article class="tip tip--2">
    <div class="tip__badge"><div class="tip__art" role="img" aria-label="Icon of information being filtered down"></div></div>
    <h3 class="tip__head">FILTER &amp; FOCUS</h3>
    <div class="tip__body">
      <p>When you try to share everything, you share nothing.</p>
      <p><strong>TIP:</strong> Start your planning with the "view" you want your audience to have at the end of the talk. Then ask yourself "What would they need to know in order to get there?"</p>
    </div>
  </article>

  <article class="tip tip--3">
    <div class="tip__badge"><div class="tip__art" role="img" aria-label="Icon of an eye over a chart"></div></div>
    <h3 class="tip__head">SHOW YOUR SCIENCE</h3>
    <div class="tip__body">
      <p>Your slides should do something for you that your words cannot. This means make your slides VISUAL not VERBAL.</p>
      <p><strong>TIP:</strong> NO BULLET POINTS (seriously!). Have a brief take-away messages supported by visual evidence.</p>
    </div>
  </article>

  <div class="tips-foot-mark"></div>
  <div class="brand brand--tips">
    <span class="brand__dot"></span>
    <span class="brand__name">Dana Whitfield</span>
  </div>
  <p class="tips-cta">Need more help? Check out Dana Whitfield's Craft Talk Studio Boot Camp training program. Includes 1:1 Coaching!</p>
</section>

</body>
</html>
```